Business Card for plorvaTEC

Create a Business Card with an existing logo for plorvaTEC AG. We are a Information Technology company that does consulting and developing SW to automate business processes. The main colors are given from the logo.

Industry/Entity Type

Business

Requirements
Nice to have
• we use a a font style Century Gothic in our documents

```html
<!DOCTYPE html>
<html lang="en">
<head>
<meta charset="utf-8">
<title>plorvaTEC – Business Card</title>
<link href="https://fonts.googleapis.com/css2?family=Questrial&family=Mulish:wght@700&display=swap" rel="stylesheet">
<style>
  :root {
    --page: #eceef1;
    --card-white: #ffffff;
    --blue-deep: #1c3f9c;
    --blue-mid: #1f6fc8;
    --blue-light: #2aa6e6;
    --green: #5cbf2a;
    --green-light: #a6dc3a;
    --ink: #555a60;
    --ink-dark: #3a3e44;
  }
  * { box-sizing: border-box; margin: 0; padding: 0; }
  html, body { width: 1200px; height: 1024px; overflow: hidden; }
  body {
    background: var(--page);
    font-family: "Questrial", sans-serif;
    display: flex;
    flex-direction: column;
    align-items: center;
    justify-content: center;
    gap: 80px;
  }
  .card {
    position: relative;
    width: 640px;
    height: 366px;
    border-radius: 24px;
    overflow: hidden;
    box-shadow: 0 10px 28px rgba(20, 40, 80, 0.18);
  }
  .card-front { background: var(--card-white); }
  .front-curves { position: absolute; inset: 0; }
  .brand {
    position: absolute;
    left: 40px;
    top: 118px;
    display: flex;
    align-items: center;
    gap: 12px;
  }
  .brand-dot {
    width: 36px; height: 36px; border-radius: 50%;
    background: var(--blue-mid);
  }
  .brand-name {
    font-size: 36px;
    color: var(--ink-dark);
    letter-spacing: -0.5px;
  }
  .holder {
    position: absolute;
    left: 400px;
    width: 220px;
    top: 92px;
    text-align: center;
  }
  .holder-name {
    font-family: "Mulish", sans-serif;
    font-weight: 700;
    font-size: 22px;
    color: #ffffff;
  }
  .holder-role {
    font-family: "Mulish", sans-serif;
    font-weight: 700;
    font-size: 16px;
    color: var(--green-light);
    margin-top: 2px;
  }
  .address {
    position: absolute;
    left: 88px;
    top: 190px;
    font-size: 15px;
    line-height: 1.3;
    color: var(--ink);
  }
  .contacts {
    position: absolute;
    left: 88px;
    top: 240px;
    list-style: none;
    font-size: 15px;
    color: var(--ink);
  }
  .contacts li { display: flex; align-items: center; gap: 8px; height: 22px; }
  .contacts svg { width: 14px; height: 14px; flex: none; }
  .card-back {
    background: radial-gradient(circle at 30% 40%, var(--blue-light) 0%, var(--blue-mid) 45%, var(--blue-deep) 100%);
  }
  .back-brand {
    position: absolute;
    left: 0; right: 0;
    top: 130px;
    display: flex;
    align-items: center;
    justify-content: center;
    gap: 20px;
  }
  .back-dot {
    width: 70px; height: 70px; border-radius: 50%;
    background: #ffffff;
  }
  .back-name {
    font-size: 78px;
    color: #ffffff;
    letter-spacing: -1px;
  }
  .back-web {
    position: absolute;
    left: 0; right: 0;
    top: 270px;
    text-align: center;
    font-size: 17px;
    color: #ffffff;
    letter-spacing: 0.5px;
  }
</style>
</head>
<body>

  <section class="card card-front">
    <svg class="front-curves" viewBox="0 0 640 366" aria-hidden="true">
      <defs>
        <linearGradient id="frontBlue" x1="0" y1="0" x2="1" y2="1">
          <stop offset="0" stop-color="#2aa6e6"/>
          <stop offset="0.5" stop-color="#1f6fc8"/>
          <stop offset="1" stop-color="#1c3f9c"/>
        </linearGradient>
      </defs>
      <path d="M340,0 C330,140 390,250 520,320 C560,342 600,356 640,366" fill="none" stroke="#5cbf2a" stroke-width="12"/>
      <path d="M372,0 C366,150 450,260 640,316 L640,0 Z" fill="url(#frontBlue)"/>
    </svg>

    <div class="brand">
      <span class="brand-dot"></span>
      <span class="brand-name">plorvaTEC</span>
    </div>

    <div class="holder">
      <p class="holder-name">Lukas Brenner</p>
      <p class="holder-role">CTO</p>
    </div>

    <p class="address">Talweg 12, 5400 Arlen,<br>Switzerland</p>

    <ul class="contacts">
      <li>
        <svg viewBox="0 0 14 14" aria-hidden="true"><path d="M3 1 L5.5 1 L6.5 4 L5 5.2 C5.8 7 7 8.2 8.8 9 L10 7.5 L13 8.5 L13 11 C13 12.2 12 13 10.8 12.8 C6 12 2 8 1.2 3.2 C1 2 1.8 1 3 1 Z" fill="#1f6fc8"/></svg>
        +41 56 210 48 60
      </li>
      <li>
        <svg viewBox="0 0 14 14" aria-hidden="true"><rect x="4" y="1" width="6" height="12" rx="1.2" fill="#1f6fc8"/><rect x="5" y="2.5" width="4" height="7" fill="#ffffff"/></svg>
        +41 79 385 27 14
      </li>
      <li>
        <svg viewBox="0 0 14 14" aria-hidden="true"><rect x="1" y="3" width="12" height="8" rx="1" fill="#1f6fc8"/><path d="M1.5 3.5 L7 8 L12.5 3.5" fill="none" stroke="#ffffff" stroke-width="1.2"/></svg>
        www.plorvatec.ch
      </li>
      <li>
        <svg viewBox="0 0 14 14" aria-hidden="true"><circle cx="7" cy="7" r="6" fill="#1f6fc8"/><ellipse cx="7" cy="7" rx="2.5" ry="6" fill="none" stroke="#ffffff" stroke-width="1"/><line x1="1" y1="7" x2="13" y2="7" stroke="#ffffff" stroke-width="1"/></svg>
        lukas.brenner@plorvatec.ch
      </li>
    </ul>
  </section>

  <section class="card card-back">
    <div class="back-brand">
      <span class="back-dot"></span>
      <span class="back-name">plorvaTEC</span>
    </div>
    <p class="back-web">www.plorvatec.ch</p>
  </section>

</body>
</html>
```